Dorn Studio 817 the new wave for sound to enlighten open ears

This is a music recording studio, we need pictures of a booth, random pictures of anything that will draw interest to a recording studio, we just need the website to reflect a music studio recording website. Apply generic information on the site that correlates with most music studio websites up to date. We want the modern style look that will entice eyes across the nation. Information should be easily accessible on the website. Dorn Studio 817 is owned by Leonard Vasquez located 6172 Bramwell Ct, Miramar, Fl, 33081. Email: Lvasquezstudio@quillmarkpost.com and best contact number to date is 417-392-7048. The sound coming out of this location will be radio ready at all times, artist come in one way and come out with more wisdom than before. Its the new way to make music the appropriate way and bring the best out of those willing to reach their peak.

Target Market(s)

Recording Artist

Industry/Entity Type

Recording Studio

Coding

Coded - Design and coding required

Number of Pages Required

1 page

Font styles to use
Sans Serif

Requirements
Must have
• Anything that gives the site a music feel
Nice to have
• microphones, booths, studio mixing desk

```html
<!DOCTYPE html>
<html lang="en">
<head>
<meta charset="utf-8">
<title>Dorn Studio 817</title>
<link rel="stylesheet" href="https://fonts.googleapis.com/css2?family=Fira+Sans:wght@400;500;600&family=Open+Sans:wght@400;600;700&display=swap">
<style>
:root{
  --red:#c9333b;
  --red-text:#d63a3f;
  --header:#2a2a2a;
  --dark:#262626;
  --footer:#232323;
  --light:#ebe9ea;
  --card:#3a3a3a;
  --card-accent:#5a2f31;
  --muted:#8b8b8b;
  --text-dark:#333;
  --white:#fff;
  --pale:#f3d9da;
}
*{box-sizing:border-box;margin:0;padding:0}
html,body{width:750px;height:1200px;overflow:hidden;background:var(--dark)}
body{position:relative;font-family:"Open Sans",sans-serif;color:var(--white)}
.abs{position:absolute}
.site-header{position:absolute;left:0;top:0;width:750px;height:68px;background:var(--header);box-shadow:0 2px 4px rgba(0,0,0,.5);z-index:3}
.brand{position:absolute;left:70px;top:0;width:76px;height:68px;background:var(--red);display:flex;align-items:center;justify-content:center;font-family:"Fira Sans",sans-serif;font-weight:600;font-size:28px;color:var(--white)}
.nav a{position:absolute;top:27px;font-weight:700;font-size:10.5px;letter-spacing:.8px;color:var(--white);text-decoration:none}
.hero{position:absolute;left:0;top:68px;width:750px;height:362px;background:
  radial-gradient(ellipse 40% 30% at 22% 22%,rgba(150,140,130,.35),transparent 70%),
  radial-gradient(ellipse 40% 30% at 78% 22%,rgba(150,140,130,.35),transparent 70%),
  radial-gradient(ellipse at 50% 40%,rgba(140,100,60,.5),transparent 60%),
  linear-gradient(180deg,#3b342f 0%,#4a3a2c 40%,#6a4a32 68%,#2c2420 100%)}
.hero::after{content:"";position:absolute;inset:0;background:rgba(20,15,12,.3)}
.hero-title{position:absolute;left:0;width:750px;top:112px;text-align:center;font-family:"Fira Sans",sans-serif;font-weight:500;font-size:27px;letter-spacing:1px;z-index:1}
.hero-lead{position:absolute;left:100px;width:550px;top:155px;text-align:center;font-family:"Fira Sans",sans-serif;font-size:13px;line-height:22px;font-weight:500;letter-spacing:.6px;z-index:1}
.btn{position:absolute;background:var(--red);color:var(--white);font-size:10.5px;font-weight:600;letter-spacing:.8px;display:flex;align-items:center;justify-content:center}
.slider-ctrl{position:absolute;left:630px;top:322px;z-index:1}
.offers{position:absolute;left:0;top:430px;width:750px;height:350px;background:var(--light)}
.offers .shadow{position:absolute;top:0;height:36px;width:240px;background:linear-gradient(180deg,rgba(0,0,0,.18),transparent)}
.offer-title{position:absolute;top:64px;width:198px;text-align:center;font-size:13.5px;color:var(--red-text);letter-spacing:.3px;font-weight:400}
.offer-img{position:absolute;top:96px;width:198px;height:108px;box-shadow:0 4px 5px rgba(0,0,0,.25)}
.offer-text{position:absolute;top:231px;width:198px;text-align:center;font-family:"Fira Sans",sans-serif;font-size:9px;line-height:12.5px;color:var(--text-dark);letter-spacing:.4px}
.col-title{position:absolute;top:822px;font-family:"Open Sans",sans-serif;font-weight:600;font-size:13.5px}
.vision-lead{position:absolute;left:72px;top:852px;width:195px;font-size:8.3px;line-height:12px;color:var(--red-text)}
.vision-body{position:absolute;left:72px;top:906px;width:195px;font-size:8.3px;line-height:12px;color:var(--muted)}
.btn-dark{position:absolute;top:1030px;height:22px;background:#3c3c3c;font-size:8px;font-weight:700;display:flex;align-items:center;justify-content:center}
.service{position:absolute;left:275px;width:196px;height:56px;border-bottom:1px solid #3e3e3e}
.service svg{position:absolute;left:2px;top:6px}
.service h4{position:absolute;left:38px;top:2px;font-size:8px;font-weight:400;color:var(--red-text)}
.service p{position:absolute;left:38px;top:13px;width:160px;font-size:8px;line-height:12px;color:var(--muted)}
.member{position:absolute;left:478px;width:197px;height:58px;background:var(--card)}
.member.accent{background:var(--card-accent)}
.member .photo{position:absolute;left:0;top:0;width:58px;height:58px;background:linear-gradient(135deg,#5a5450,#1c1c1c)}
.member h4{position:absolute;left:71px;top:11px;font-size:11px;font-weight:400;color:var(--red-text)}
.member p{position:absolute;left:71px;top:25px;width:125px;font-size:8px;line-height:12px;color:var(--white)}
.contact-band{position:absolute;left:0;top:1094px;width:750px;height:63px;background:var(--red)}
.address{position:absolute;left:102px;top:18px;font-family:"Fira Sans",sans-serif;font-size:9px;line-height:13px;font-weight:500;letter-spacing:.5px}
.call{position:absolute;left:466px;top:25px;font-size:10.5px;font-weight:700}
.call span{margin-left:6px;letter-spacing:.8px;color:var(--pale)}
.site-footer{position:absolute;left:0;top:1157px;width:750px;height:43px;background:var(--footer)}
.copyright{position:absolute;left:70px;top:16px;font-family:"Fira Sans",sans-serif;font-size:10px;font-weight:500;letter-spacing:.5px;color:#ddd}
.social{position:absolute;top:17px;width:11px;height:11px;border-radius:50%;background:#555}
</style>
</head>
<body>

<header class="site-header">
  <div class="brand">817</div>
  <nav class="nav">
    <a style="left:272px">HOME</a>
    <a style="left:335px">STUDIO</a>
    <a style="left:406px">EQUIPMENT</a>
    <a style="left:500px">RATES &amp; SERVICES</a>
    <a style="left:627px">CONTACT</a>
  </nav>
</header>

<section class="hero" role="img" aria-label="Photo of a recording studio control room with a large mixing desk and studio monitors">
  <h1 class="hero-title">We are waiting to hear from you</h1>
  <p class="hero-lead">Lorem ipsum dolor sit amet conse ctetur adipisicing elit, sed do eiusmod tempor dolore magna aliqua. Ut enim ad minim veniam</p>
  <div class="btn" style="left:306px;top:229px;width:130px;height:26px;z-index:1">READ MORE</div>
  <svg class="slider-ctrl" width="34" height="16" viewBox="0 0 34 16">
    <rect x="0" y="1" width="5" height="14" fill="#fff"/><rect x="8" y="1" width="5" height="14" fill="#fff"/>
    <path d="M20 1 L33 8 L20 15 Z" fill="#fff"/>
  </svg>
</section>

<section class="offers">
  <div class="shadow" style="left:0"></div>
  <div class="shadow" style="left:505px"></div>
  <h3 class="offer-title" style="left:71px">RECORDING PRICE</h3>
  <h3 class="offer-title" style="left:275px">MEMBERSHIPS DEALS</h3>
  <h3 class="offer-title" style="left:479px">MIX DOWN ONLY PRICES</h3>
  <div class="offer-img" style="left:71px;background:radial-gradient(circle at 65% 40%,rgba(220,140,150,.7),transparent 55%),linear-gradient(120deg,#7a5c9c,#a985a8 55%,#8c7cb4)" role="img" aria-label="Purple artwork of music notes"></div>
  <div class="offer-img" style="left:275px;background:radial-gradient(ellipse at 50% 25%,rgba(255,220,140,.6),transparent 50%),linear-gradient(180deg,#3a3226 0%,#b98a2a 45%,#e3b43c 75%,#8a6a2a 100%)" role="img" aria-label="Close-up of mixing desk faders"></div>
  <div class="offer-img" style="left:479px;background:radial-gradient(circle at 85% 20%,rgba(255,235,160,.8),transparent 45%),linear-gradient(120deg,#3b3270,#5b4a7a 50%,#c9a25a 100%)" role="img" aria-label="Hand playing an electric guitar"></div>
  <p class="offer-text" style="left:71px">Lorem ipsum dolor sit amet conse ctetur dolore magna aliqua. Ut enim ad.</p>
  <p class="offer-text" style="left:275px">Lorem ipsum dolor sit amet conse ctetur dolore magna aliqua. Ut enim ad.</p>
  <p class="offer-text" style="left:479px">Lorem ipsum dolor sit amet conse ctetur dolore magna aliqua. Ut enim ad.</p>
  <div class="btn" style="left:309px;top:280px;width:130px;height:32px">GET STARTED</div>
</section>

<h3 class="col-title" style="left:72px">OUR VISION</h3>
<h3 class="col-title" style="left:275px">SERVICES</h3>
<h3 class="col-title" style="left:478px">OUR TEAM</h3>

<p class="vision-lead">Lorem ipsum dolor sit amet conse ctetur adipisicing elit, sed do eiusmod tempor incididunt ut labore et dolore magna aliqua. Ut enim ad minim veniam quis nostrud</p>
<p class="vision-body">Sit amet conse ctetur adipisicing elit, sed do eiusmod tempor incididunt ut labore et dolore magna aliqua. Ut enim ad minim veniam, quis nostrud exercitation ullamco laboris nisi ut aliquip ex ea commodo consequat. Duis aute irure dolor in reprehenderit in voluptate velit esse cillum dolore eu fugiat nulla pariatur. Excepteur sint occaecat cupidatat non proident, sunt in culpa qui officia deserunt.</p>
<div class="btn-dark" style="left:72px;width:66px">READ MORE</div>

<div class="service" style="top:852px">
  <svg width="26" height="34" viewBox="0 0 26 34"><rect x="8" y="0" width="10" height="20" rx="5" fill="#5a5a5a"/><path d="M3 14 a10 10 0 0 0 20 0" stroke="#5a5a5a" stroke-width="2.5" fill="none"/><rect x="12" y="24" width="2.5" height="7" fill="#5a5a5a"/><rect x="6" y="31" width="14" height="2.5" fill="#5a5a5a"/></svg>
  <h4>LOREM IPSUM DOLOR SIT</h4>
  <p>Sit amet conse ctetur adipisicing elit, sed do eiusmod tempor incididunt.</p>
</div>
<div class="service" style="top:908px">
  <svg width="26" height="34" viewBox="0 0 26 34"><path d="M0 8 L11 17 L0 26 Z M11 8 L22 17 L11 26 Z" fill="#5a5a5a"/><rect x="22" y="8" width="3" height="18" fill="#5a5a5a"/></svg>
  <h4>SIT AMET CONSE CTETUR</h4>
  <p>Sit amet conse ctetur adipisicing elit, sed do eiusmod tempor incididunt.</p>
</div>
<div class="service" style="top:964px">
  <svg width="26" height="34" viewBox="0 0 26 34"><path d="M9 6 L25 2 L25 24" stroke="#5a5a5a" stroke-width="3" fill="none"/><rect x="8" y="5" width="3" height="22" fill="#5a5a5a"/><ellipse cx="6" cy="28" rx="5.5" ry="4" fill="#5a5a5a"/><ellipse cx="20" cy="25" rx="5.5" ry="4" fill="#5a5a5a"/></svg>
  <h4>ADIPISICING ELIT</h4>
  <p>Sit amet conse ctetur adipisicing elit, sed do eiusmod tempor incididunt.</p>
</div>
<div class="btn-dark" style="left:275px;width:67px">READ MORE</div>

<div class="member" style="top:854px">
  <div class="photo" role="img" aria-label="Portrait of a team member"></div>
  <h4>EXCEPTEUR SINT</h4>
  <p>Sit amet conse ctetur<br>adipisicing elit sed do eiusmod</p>
</div>
<div class="member" style="top:918px">
  <div class="photo" role="img" aria-label="Portrait of a team member"></div>
  <h4>LOREM IPSUM</h4>
  <p>Sit amet conse ctetur<br>adipisicing elit sed do eiusmod</p>
</div>
<div class="member accent" style="top:982px">
  <div class="photo" role="img" aria-label="Portrait of a team member"></div>
  <h4>DOLOR SIT AMET</h4>
  <p>Sit amet conse ctetur<br>adipisicing elit sed do eiusmod</p>
</div>

<section class="contact-band">
  <svg class="abs" style="left:70px;top:18px" width="20" height="28" viewBox="0 0 20 28"><path d="M10 0 A10 10 0 0 1 20 10 C20 17 10 28 10 28 C10 28 0 17 0 10 A10 10 0 0 1 10 0 Z" fill="#fff"/><circle cx="10" cy="10" r="4" fill="var(--red)"/></svg>
  <p class="address">Dorn Studio 817 is owned by Leonard Vasquez located 6172<br>Bramwell Ct, Miramar, Fl, 33081</p>
  <svg class="abs" style="left:431px;top:17px" width="26" height="26" viewBox="0 0 24 24"><path d="M6.6 10.8c1.4 2.8 3.8 5.1 6.6 6.6l2.2-2.2c.3-.3.7-.4 1-.2 1.1.4 2.3.6 3.6.6.6 0 1 .4 1 1V20c0 .6-.4 1-1 1C10.6 21 3 13.4 3 4c0-.6.4-1 1-1h3.5c.6 0 1 .4 1 1 0 1.3.2 2.5.6 3.6.1.3 0 .7-.2 1l-2.3 2.2z" fill="#fff"/></svg>
  <p class="call">CALL US NOW TOLL FREE: <span>417-392-7048</span></p>
</section>

<footer class="site-footer">
  <p class="copyright">Lvasquezstudio &nbsp;© 2017. &nbsp;Privacy Policy</p>
  <span class="social" style="left:564px"></span>
  <span class="social" style="left:587px"></span>
  <span class="social" style="left:610px"></span>
  <span class="social" style="left:633px"></span>
  <span class="social" style="left:656px"></span>
  <svg class="abs" style="left:703px;top:10px" width="14" height="14" viewBox="0 0 14 14"><circle cx="7" cy="7" r="7" fill="var(--red)"/><path d="M3.5 8.5 L7 5 L10.5 8.5" stroke="#fff" stroke-width="2" fill="none"/></svg>
</footer>

</body>
</html>
```